Marla Tesch Wordpress site

I want a word press website design for my current site. Current site can be found at www.velquora.com and marlatesch.com Velquora is a consulting company that does strategic planning for start ups and emerging companies who are transitioning to their next level of growth. My target market includes start ups that are considering early stage and first round capital raises as well as municipalities looking for feasibility studies and/or financial opinions on large capital projects.My core business is around finance, budgeting, money and how to manage or obtain it.

My business is to create financial models for early stage businesses as well as provide risk analysis studies, feasibility studies, and strategic consulting. I also speak and write.

This means that I want my web presence to have a more corporate clean look as opposed to the more creative. Our industry colleagues would be commercial banks, Venture Capital firms, Consulting firms, Angel investor groups, and private equity firms.

I'd like to be able to add blogs and video to the site as well as keep the current content. Since I am also an author and I write books about fiance and business, I'd like to be able to sell books from the site. I'd also like to be able to capture email addresses or have potential client send me a question from the site.

I have included the company logo which was designed in Adobe Illustrator as well as personal photos included on the MarlaTesch site

Target Market(s)

Banks, municipalities, Venture capitalist, early stage start ups, entrepreneurs raising capital, angel investors, small businesses. consulting firms,private equity firms, radio stations, and television media

Number of Pages Required

2 page

Font styles to use
Sans Serif

Requirements
Must have
• Header, company logo, ability to load video, ability to load blogs, links to social media sites, ability to leave contact info or ask questions as well as a place where I can drop in items to sell like my e-book products.
• Please take a look at both sites: Velquora.com and MarlaTesch.com I'm combining these two sites.
• Neutral colors--calming
Should not have
• Do not use the "simply Marla" logo. Don't have to use the simplymarla colors.

```html
<!DOCTYPE html>
<html lang="en">
<head>
<meta charset="utf-8">
<title>Velquora Associates</title>
<link rel="stylesheet" href="https://fonts.googleapis.com/css2?family=Open+Sans:wght@400;600;700&display=swap">
<style>
:root{
  --red:#b8321d;
  --red-dark:#8e2615;
  --brown:#6e2a1b;
  --brown-deep:#4f1d12;
  --ink:#333;
  --muted:#777;
  --light:#f0f0f0;
  --line:#ddd;
  --white:#fff;
}
*{box-sizing:border-box;margin:0;padding:0}
html,body{width:735px;height:1200px;overflow:hidden;background:var(--white)}
body{font-family:"Open Sans",Arial,sans-serif;color:var(--ink);position:relative}
.site-header{height:34px;display:flex;align-items:center;justify-content:space-between;padding:0 22px}
.brand{display:flex;align-items:center;gap:6px}
.brand-mark{width:16px;height:16px;background:var(--red)}
.brand-name{font-size:17px;font-weight:700;color:var(--brown)}
.header-tools{display:flex;gap:6px;align-items:center}
.search{width:82px;height:14px;border:1px solid var(--line);font-size:6px;color:#999;padding:2px 4px}
.login{background:var(--red);color:#fff;font-size:6px;font-weight:700;padding:3px 7px}
.main-nav{height:16px;background:var(--brown);display:flex;padding-left:22px}
.main-nav a{color:#fff;text-decoration:none;font-size:6px;font-weight:600;padding:0 11px;line-height:16px}
.main-nav a.active{background:var(--red)}
.hero{position:relative;height:200px;background:linear-gradient(90deg,#d9d3cc,#b9aea3 55%,#c9bfb4)}
.hero-photo{position:absolute;right:60px;top:0;width:290px;height:200px;background:linear-gradient(120deg,#6d4a36,#caa58b 55%,#e3d3c4)}
.hero-caption{position:absolute;left:40px;top:50px;width:260px;background:rgba(255,255,255,.92);padding:12px 14px}
.hero-caption p{font-size:13px;font-weight:600;line-height:1.35;color:#222}
.btn{display:inline-block;background:var(--red);color:#fff;font-size:7px;font-weight:700;padding:5px 10px;margin-top:9px}
.intro-strip{background:var(--light);height:30px;padding:6px 40px;font-size:5.5px;color:var(--muted);line-height:1.45}
.section-title{text-align:center;font-size:11px;font-weight:700;color:var(--brown);letter-spacing:.5px}
.about-company{padding-top:14px}
.about-company .lead{width:560px;margin:6px auto 0;text-align:center;font-size:6px;color:var(--muted);line-height:1.5}
.services{display:flex;justify-content:center;gap:70px;margin-top:20px}
.service{width:90px;text-align:center}
.service-icon{width:46px;height:46px;background:var(--red);margin:0 auto 8px;display:flex;align-items:center;justify-content:center}
.service span{font-size:7px;color:#444;line-height:1.3;display:block}
.about-person{position:absolute;top:468px;left:0;width:735px;height:184px;background:var(--light)}
.about-person .text{position:absolute;left:40px;top:14px;width:380px}
.about-person h2{font-size:11px;color:var(--red);font-weight:700}
.about-person p{font-size:6px;color:#555;line-height:1.5;margin-top:6px}
.person-photo{position:absolute;right:60px;top:0;width:230px;height:184px;background:linear-gradient(135deg,#c9b9a6,#5b3a2a 60%,#8a6a55)}
.media{position:absolute;top:672px;left:40px;width:655px;display:flex;gap:30px}
.media h3{font-size:11px;font-weight:700;color:var(--brown);margin-bottom:8px}
.videos{width:290px}
.video-frame{height:150px;background:linear-gradient(160deg,#111,#3b3b3b 60%,#1a1a1a);position:relative}
.play{position:absolute;left:50%;top:50%;transform:translate(-50%,-50%)}
.articles{flex:1}
.article{display:flex;gap:8px;margin-bottom:10px}
.thumb{width:58px;height:42px;flex:none}
.article h4{font-size:8px;color:#333;font-weight:700}
.article .date{font-size:6px;color:var(--red);margin:2px 0}
.article p{font-size:5.5px;color:var(--muted);line-height:1.4}
.site-footer{position:absolute;top:930px;left:0;width:735px;height:240px;background:var(--brown);color:#fff;padding:18px 40px;display:flex;gap:30px}
.site-footer h5{font-size:8px;font-weight:700;margin-bottom:8px}
.footer-links{width:160px}
.footer-links ul{list-style:none;columns:2;font-size:6px;line-height:2}
.recent{width:200px}
.recent ul{list-style:none;font-size:6px;line-height:2}
.newsletter{flex:1}
.newsletter input{display:block;width:100%;height:14px;border:0;margin-bottom:5px;font-size:6px;padding:0 4px;font-family:inherit}
.newsletter .btn{margin-top:2px}
.social{display:flex;gap:4px;margin-top:30px}
.social i{width:12px;height:12px;background:var(--red-dark);display:block}
.copyright{position:absolute;top:1170px;left:0;width:735px;height:30px;background:var(--brown-deep);color:#d9c3bb;font-size:6px;line-height:30px;padding-left:40px}
</style>
</head>
<body>
<header class="site-header">
  <div class="brand"><span class="brand-mark"></span><span class="brand-name">Velquora</span></div>
  <div class="header-tools"><div class="search">Search</div><div class="login">LOG IN</div></div>
</header>
<nav class="main-nav">
  <a class="active">HOME</a><a>WHAT WE DO</a><a>ABOUT MARLA</a><a>OUR CLIENTS</a><a>THE VIDEOS</a><a>NEWS</a><a>ARTICLES</a><a>VIDEOS</a><a>CONTACT US</a>
</nav>
<section class="hero">
  <div class="hero-photo" role="img" aria-label="Portrait photo of Marla Tesch smiling"></div>
  <div class="hero-caption">
    <p>We are consulting company that does strategic planning for start ups and emerging companies who are transitioning to their next level of growth..</p>
    <span class="btn">READ MORE</span>
  </div>
</section>
<div class="intro-strip">We guide founders through budgets, capital raises and growth plans with clear models and honest advice. Our team pairs financial rigor with practical strategy so every decision is backed by numbers you can trust and explain to investors, lenders and boards.</div>
<section class="about-company">
  <h2 class="section-title">ABOUT OUR COMPANY</h2>
  <p class="lead">Velquora Associates builds financial models, feasibility studies and risk analysis for early stage businesses and public bodies. We help leaders plan funding rounds, test large capital projects and manage money with calm, steady confidence at every stage of growth.</p>
  <div class="services">
    <div class="service"><div class="service-icon"><svg width="24" height="24" viewBox="0 0 24 24" fill="none" stroke="#fff" stroke-width="2"><path d="M3 20h18M6 16v-4M11 16V8M16 16v-6M3 10l6-5 5 3 7-5"/></svg></div><span>Improve Overall Business Strategy &amp; Planning</span></div>
    <div class="service"><div class="service-icon"><svg width="24" height="24" viewBox="0 0 24 24" fill="none" stroke="#fff" stroke-width="2"><circle cx="8" cy="8" r="3"/><circle cx="16" cy="8" r="3"/><path d="M2 20c1-4 4-6 6-6s5 2 6 6M12 20c1-4 3-6 4-6s4 2 6 6"/></svg></div><span>Affect Leadership Development</span></div>
    <div class="service"><div class="service-icon"><svg width="24" height="24" viewBox="0 0 24 24" fill="none" stroke="#fff" stroke-width="2"><rect x="3" y="6" width="18" height="12"/><circle cx="12" cy="12" r="3"/></svg></div><span>Raise Capital Funds</span></div>
    <div class="service"><div class="service-icon"><svg width="24" height="24" viewBox="0 0 24 24" fill="none" stroke="#fff" stroke-width="2"><path d="M12 3l8 3v6c0 5-4 8-8 9-4-1-8-4-8-9V6z"/><path d="M8 12l3 3 5-6"/></svg></div><span>Angel Investor Groups</span></div>
  </div>
</section>
<section class="about-person">
  <div class="text">
    <h2>ABOUT MARLA</h2>
    <p>As long as I can remember I have loved numbers and the stories they tell. Growing up, I watched family members build small firms and learned how careful planning shapes every outcome for people and places.</p>
    <p>That early lesson became a career in finance, budgeting and strategy. Today I help founders and cities plan capital, weigh risk and grow with purpose. I also speak, write books and share practical guidance for leaders at every stage.</p>
    <span class="btn">More About Her</span>
  </div>
  <div class="person-photo" role="img" aria-label="Photo of Marla Tesch"></div>
</section>
<section class="media">
  <div class="videos">
    <h3>WATCH VIDEOS</h3>
    <div class="video-frame" role="img" aria-label="Video still of a speaker">
      <svg class="play" width="30" height="30" viewBox="0 0 30 30"><circle cx="15" cy="15" r="14" fill="rgba(255,255,255,.25)"/><path d="M12 9l9 6-9 6z" fill="#fff"/></svg>
    </div>
  </div>
  <div class="articles">
    <h3>RECENT ARTICLES</h3>
    <div class="article"><div class="thumb" role="img" aria-label="Article image, blue sky" style="background:linear-gradient(135deg,#3a6fb0,#9cc3e6)"></div><div><h4>Heaven's Wastebaskets</h4><div class="date">May 18, 2015</div><p>In this country we spend nearly four billion a year on waste management, and a lot of it never needs to leave the source at all.</p></div></div>
    <div class="article"><div class="thumb" role="img" aria-label="Article image, sunset" style="background:linear-gradient(135deg,#d9772b,#f3c46a)"></div><div><h4>Heaven's Wastebaskets</h4><div class="date">May 18, 2015</div><p>In this country we spend nearly four billion a year on waste management, and a lot of it never needs to leave the source at all.</p></div></div>
    <div class="article"><div class="thumb" role="img" aria-label="Article image, red tones" style="background:linear-gradient(135deg,#8e1f1f,#d14b3a)"></div><div><h4>Heaven's Wastebaskets</h4><div class="date">May 18, 2015</div><p>In this country we spend nearly four billion a year on waste management, and a lot of it never needs to leave the source at all.</p></div></div>
  </div>
</section>
<footer class="site-footer">
  <div class="footer-links"><h5>QUICK LINKS</h5><ul><li>Home</li><li>What We Do</li><li>About Marla</li><li>Our Clients</li><li>The Videos</li><li>News</li><li>Articles</li><li>Videos</li><li>Contact Us</li></ul></div>
  <div class="recent"><h5>RECENT POSTS</h5><ul><li>The Bootstrap Founder &amp; You</li><li>Planning for the Next Round</li><li>The Depth of an Honest Budget</li><li>Funding Growth With Care</li><li>Reading Risk in Public Projects</li><li>Notes From the Speaking Tour</li></ul></div>
  <div class="newsletter"><h5>NEWSLETTER SUBSCRIBE</h5><input value="Your Name" readonly><input value="Your Email" readonly><span class="btn">Sign Up</span>
    <div class="social"><i></i><i></i><i></i><i></i><i></i><i></i></div></div>
</footer>
<div class="copyright">Copyright 2015 © Velquora Associates. All Rights Reserved.</div>
</body>
</html>
```